Social Media Graphics - Harbor Climb REVISED

Create 6-7 individual social media graphics (square size) to encourage folks to join our online course called:

The Lantern Ledger Plan
How to Launch a Multi-Million Business From Scratch
Sign Up Today!

IMPORTANT: Make the largest and most prominent text on the graphic be: How to Launch a Multi-Million Business From Scratch

For the color scheme of the graphics, let's try a blue color palette; make sure the graphics appeal to both men and women

Make sure each graphic contains 1 of the 3 pics attached (crop pic as needed); and make sure one of the graphics is all TEXT only.

Target Market(s)

men and women looking to start a business

Industry/Entity Type

Entrepreneurship

Colors
0054AA
0677BA
7BADD7
CADEEF
E8F1F8

Requirements
Must have
• All the text and use the 3 pics provided; one graphic can be all text; Simple, modern design that's easy to read

```html
<!DOCTYPE html>
<html lang="en">
<head>
<meta charset="utf-8">
<title>The Lantern Ledger Plan – Social Graphics Set</title>
<link rel="stylesheet" href="https://fonts.googleapis.com/css2?family=Bebas+Neue&family=Poppins:wght@600;800&family=Roboto:wght@300;400&display=swap">
<style>
  :root {
    --page: #f3f4f6;
    --sky: #45b8f2;
    --blue: #0a63b8;
    --navy: #0c4a94;
    --deep: #0c3f7f;
    --ink-blue: #0a55a8;
    --white: #ffffff;
    --pale: #cadeef;
    --mist: #7badd7;
  }
  * { box-sizing: border-box; margin: 0; padding: 0; }
  html, body { width: 1200px; height: 825px; overflow: hidden; background: var(--page); }
  .board { position: relative; width: 1200px; height: 825px; }

  .tile {
    position: absolute; width: 349px; height: 349px; overflow: hidden;
    background: linear-gradient(180deg, var(--sky) 0%, var(--blue) 35%, var(--navy) 100%);
    color: var(--white);
  }
  .tile--1 { left: 49px; top: 50px; }
  .tile--2 { left: 425px; top: 50px; }
  .tile--3 { left: 802px; top: 50px; }
  .tile--4 { left: 49px; top: 426px; }
  .tile--5 { left: 425px; top: 426px; }
  .tile--6 { left: 802px; top: 426px; }

  /* soft photo areas */
  .photo { position: absolute; }
  .photo--duo-stage {
    background:
      radial-gradient(ellipse 30% 55% at 25% 45%, rgba(202,222,239,.45), rgba(123,173,215,.15) 60%, transparent 80%),
      radial-gradient(ellipse 30% 55% at 60% 45%, rgba(202,222,239,.4), rgba(123,173,215,.15) 60%, transparent 80%),
      linear-gradient(180deg, rgba(12,74,148,.35) 0%, rgba(12,74,148,0) 100%);
  }
  .photo--duo-mono {
    background:
      radial-gradient(ellipse 35% 50% at 35% 40%, rgba(220,228,238,.55), rgba(150,170,195,.25) 55%, transparent 80%),
      radial-gradient(ellipse 32% 48% at 72% 48%, rgba(220,228,238,.5), rgba(150,170,195,.22) 55%, transparent 80%);
  }
  .photo--solo-mono {
    background: radial-gradient(ellipse 45% 55% at 45% 45%, rgba(210,222,236,.55), rgba(140,165,195,.25) 55%, transparent 80%);
  }
  .photo--solo-warm {
    background:
      radial-gradient(ellipse 35% 25% at 50% 22%, rgba(120,60,60,.45), transparent 80%),
      radial-gradient(ellipse 55% 40% at 60% 65%, rgba(190,50,120,.6), rgba(150,60,140,.25) 60%, transparent 85%);
  }

  .brand {
    position: absolute; font-family: "Poppins", sans-serif; font-weight: 800;
    font-size: 14px; line-height: 1.05; text-transform: uppercase; color: var(--white);
  }
  .notch { position: absolute; width: 24px; height: 24px; border-radius: 50%; background: var(--white); }

  .kicker { position: absolute; font-family: "Roboto", sans-serif; font-weight: 300; text-transform: uppercase; white-space: nowrap; }
  .headline {
    position: absolute; font-family: "Bebas Neue", sans-serif; font-weight: 400; text-transform: uppercase;
    white-space: nowrap; text-shadow: 0 2px 6px rgba(0,0,0,.25);
  }
  .cta-card {
    position: absolute; background: var(--white); color: var(--ink-blue);
    font-family: "Bebas Neue", sans-serif; text-transform: uppercase;
    font-size: 37px; line-height: 30px; text-align: center; padding-top: 16px;
    border-radius: 24px 24px 0 0;
  }
  .cta-frame {
    position: absolute; border: 1.5px solid var(--white);
    font-family: "Bebas Neue", sans-serif; text-transform: uppercase;
    font-size: 28px; line-height: 24px; text-align: center;
  }
  .deco { position: absolute; inset: 0; width: 349px; height: 349px; }

  /* Tile 1 */
  .tile--1 .brand { left: 230px; top: 13px; }
  .tile--1 .notch { right: -12px; top: 16px; }
  .tile--1 .kicker { left: 20px; top: 164px; font-size: 21px; }
  .tile--1 .headline { left: 20px; top: 191px; font-size: 64px; line-height: 54px; }
  .tile--1 .tagline { position: absolute; left: 21px; top: 304px; font-family: "Roboto", sans-serif; font-size: 14px; }
  .tile--1 .cta-card { left: 220px; top: 265px; width: 115px; height: 90px; }

  /* Tile 2 */
  .tile--2 .brand-outline {
    position: absolute; left: 0; right: 0; top: 14px; text-align: center;
    font-family: "Poppins", sans-serif; font-weight: 600; font-size: 38px; line-height: 1.15;
    text-transform: uppercase; color: transparent; -webkit-text-stroke: 1.5px rgba(255,255,255,.9);
  }
  .tile--2 .brand { left: 22px; top: 142px; }
  .tile--2 .notch { left: -12px; top: 145px; }
  .label {
    position: absolute; left: 108px; top: 216px; width: 136px; height: 26px; background: var(--white);
    color: var(--ink-blue); font-family: "Bebas Neue", sans-serif; font-size: 21px; letter-spacing: 2px;
    text-align: center; line-height: 27px; text-transform: uppercase;
  }
  .badge {
    position: absolute; left: 277px; top: 185px; width: 56px; height: 56px; border-radius: 50%;
    border: 1.5px solid var(--white); font-family: "Roboto", sans-serif; font-weight: 400; font-size: 8.5px;
    text-align: center; line-height: 1.25; padding-top: 17px; text-transform: uppercase;
  }
  .tile--2 .headline { left: 0; right: 0; text-align: center; line-height: 1; }
  .tile--2 .headline--a { top: 252px; font-size: 39px; }
  .tile--2 .headline--b { top: 289px; font-size: 47px; }

  /* Tile 3 */
  .tile--3 .brand { left: 14px; top: 19px; }
  .tile--3 .notch { left: -12px; top: 20px; }
  .tile--3 .kicker { right: 15px; top: 189px; font-size: 16px; }
  .tile--3 .headline { right: 15px; top: 215px; font-size: 50px; line-height: 40px; text-align: right; }
  .tile--3 .cta-frame { left: 14px; top: 265px; width: 81px; height: 100px; border-radius: 12px 12px 0 0; padding-top: 12px; }

  /* Tile 4 */
  .tile--4 .kicker { right: 14px; top: 41px; font-size: 16px; }
  .tile--4 .headline { right: 14px; top: 66px; font-size: 48px; line-height: 40px; text-align: right; }
  .tile--4 .brand { left: 19px; top: 303px; }
  .tile--4 .notch { left: -12px; top: 306px; }
  .tile--4 .cta-card { left: 220px; top: 255px; width: 115px; height: 100px; }

  /* Tile 5 */
  .tile--5 .cta-frame { left: 24px; top: -2px; width: 80px; height: 83px; border-radius: 0 0 12px 12px; padding-top: 18px; }
  .tile--5 .brand { left: 229px; top: 14px; }
  .tile--5 .notch { right: -12px; top: 22px; }
  .tile--5 .kicker { left: 23px; top: 155px; font-size: 17px; }
  .tile--5 .headline { left: 23px; top: 184px; font-size: 56px; line-height: 50px; }

  /* Tile 6 */
  .tile--6 .brand { left: 0; right: 0; top: 18px; text-align: center; }
  .tile--6 .kicker { left: 0; right: 0; top: 80px; font-size: 18px; text-align: center; }
  .tile--6 .headline { left: 0; right: 0; top: 108px; font-size: 56px; line-height: 50px; text-align: center; }
  .rule { position: absolute; left: 152px; top: 258px; width: 143px; height: 3px; background: var(--white); }
  .pill {
    position: absolute; left: 94px; top: 289px; width: 161px; height: 33px; border-radius: 17px;
    background: var(--deep); border: 2px solid var(--white); font-family: "Poppins", sans-serif;
    font-weight: 600; font-size: 13px; text-align: center; line-height: 29px; text-transform: uppercase;
  }
</style>
</head>
<body>
<main class="board">

  <section class="tile tile--1">
    <div class="photo photo--duo-stage" style="left:0;top:0;width:349px;height:240px" role="img" aria-label="Photo of the two course hosts presenting on stage in front of a city skyline with rising arrows"></div>
    <p class="brand">The Lantern<br>Ledger Plan</p>
    <span class="notch"></span>
    <p class="kicker">How to launch a</p>
    <h2 class="headline">Multi-Million<br>Business</h2>
    <p class="tagline">FROM SCRATCH</p>
    <div class="cta-card">Sign up<br>today!</div>
  </section>

  <section class="tile tile--2">
    <p class="brand-outline">The Lantern<br>Ledger Plan</p>
    <div class="photo photo--duo-mono" style="left:0;top:40px;width:349px;height:260px" role="img" aria-label="Black and white portrait of the two course hosts smiling side by side"></div>
    <p class="brand">The Lantern<br>Ledger Plan</p>
    <span class="notch"></span>
    <div class="label">How to launch</div>
    <div class="badge">Sign up<br>today!</div>
    <h2 class="headline headline--a">Multi-Million Business</h2>
    <p class="headline headline--b">From Scratch</p>
  </section>

  <section class="tile tile--3">
    <div class="photo photo--duo-mono" style="left:80px;top:10px;width:269px;height:300px" role="img" aria-label="Black and white portrait of the two course hosts smiling"></div>
    <p class="brand">The Lantern<br>Ledger Plan</p>
    <span class="notch"></span>
    <p class="kicker">How to launch a</p>
    <h2 class="headline">Multi-Million<br>Business<br>From Scratch</h2>
    <div class="cta-frame">Sign up<br>today!</div>
  </section>

  <section class="tile tile--4">
    <div class="photo photo--solo-mono" style="left:0;top:20px;width:250px;height:329px" role="img" aria-label="Photo of the male host speaking into a microphone"></div>
    <p class="kicker">How to launch a</p>
    <h2 class="headline">Multi-Million<br>Business<br>From<br>Scratch</h2>
    <p class="brand">The Lantern<br>Ledger Plan</p>
    <span class="notch"></span>
    <div class="cta-card">Sign up<br>today!</div>
  </section>

  <section class="tile tile--5">
    <svg class="deco" viewBox="0 0 349 349" aria-hidden="true">
      <circle cx="250" cy="260" r="190" fill="none" stroke="rgba(255,255,255,.08)" stroke-width="30"/>
    </svg>
    <div class="photo photo--solo-warm" style="left:160px;top:10px;width:189px;height:339px" role="img" aria-label="Photo of the female host in a magenta top with arms crossed"></div>
    <div class="cta-frame">Sign up<br>today!</div>
    <p class="brand">The Lantern<br>Ledger Plan</p>
    <span class="notch"></span>
    <p class="kicker">How to launch a</p>
    <h2 class="headline">Multi-Million<br>Business<br>From Scratch</h2>
  </section>

  <section class="tile tile--6">
    <svg class="deco" viewBox="0 0 349 349" aria-hidden="true">
      <path d="M0 0 H349 V8 Q175 -6 0 8 Z" fill="#ffffff"/>
      <ellipse cx="175" cy="395" rx="200" ry="85" fill="#ffffff"/>
    </svg>
    <p class="brand">The Lantern<br>Ledger Plan</p>
    <p class="kicker">How to launch a</p>
    <h2 class="headline">Multi-Million<br>Business<br>From Scratch</h2>
    <span class="rule"></span>
    <div class="pill">Sign up today!</div>
  </section>

</main>
</body>
</html>
```